Recipe Card Design

I have a small kitchen store in Livingston Montana, and I would like to have recipe cards (4x6 postcard) designed with my logo, lines for recipe writing, all in black and white. My website is here: www.brambleforkpantry.com

Store

```html
<!DOCTYPE html>
<html lang="en">
<head>
<meta charset="utf-8">
<title>Recipe Card – Bramble Fork Pantry</title>
<link rel="stylesheet" href="https://fonts.googleapis.com/css2?family=Cinzel:wght@600&family=Oswald:wght@700&family=Open+Sans:wght@400&display=swap">
<style>
  :root {
    --ink: #000000;
    --paper: #ffffff;
  }
  html, body {
    margin: 0;
    padding: 0;
    width: 1200px;
    height: 929px;
    overflow: hidden;
    background: var(--paper);
  }
  .card {
    position: relative;
    width: 1200px;
    height: 929px;
    background: var(--paper);
    color: var(--ink);
  }
  .brand-rule {
    position: absolute;
    left: 66px;
    top: 52px;
    width: 620px;
    height: 4px;
    background: var(--ink);
  }
  .brand-block {
    position: absolute;
    left: 62px;
    top: 62px;
    width: 632px;
    height: 740px;
    display: flex;
    flex-direction: column;
    align-items: center;
    justify-content: center;
    gap: 6px;
  }
  .brand-mark {
    width: 120px;
    height: 120px;
    background: var(--ink);
    margin-bottom: 34px;
  }
  .brand-name {
    margin: 0;
    font-family: "Cinzel", serif;
    font-weight: 600;
    font-size: 96px;
    line-height: 1.05;
    text-align: center;
    color: var(--ink);
    letter-spacing: 2px;
  }
  .brand-place {
    position: absolute;
    left: 54px;
    top: 822px;
    width: 640px;
    margin: 0;
    font-family: "Cinzel", serif;
    font-weight: 600;
    font-size: 30px;
    letter-spacing: 5px;
    text-align: center;
    white-space: nowrap;
    color: var(--ink);
  }
  .label {
    position: absolute;
    margin: 0;
    font-family: "Oswald", sans-serif;
    font-weight: 700;
    text-transform: uppercase;
    color: var(--ink);
    line-height: 1;
  }
  .label--recipe { left: 696px; top: 64px; font-size: 52px; letter-spacing: 1px; }
  .label--ingredients { left: 700px; top: 203px; font-size: 25px; }
  .label--instructions { left: 716px; top: 367px; font-size: 25px; }
  .write-line {
    position: absolute;
    height: 3px;
    background: var(--ink);
  }
  .website {
    position: absolute;
    right: 36px;
    top: 876px;
    margin: 0;
    font-family: "Open Sans", sans-serif;
    font-size: 16px;
    color: var(--ink);
  }
</style>
</head>
<body>
<main class="card">
  <div class="brand-rule"></div>
  <div class="brand-block">
    <div class="brand-mark"></div>
    <p class="brand-name">Bramble<br>Fork<br>Pantry</p>
  </div>
  <p class="brand-place">Copper Ridge, Westmark</p>

  <h1 class="label label--recipe">Recipe</h1>
  <div class="write-line" style="left:910px;top:108px;width:244px"></div>
  <div class="write-line" style="left:706px;top:163px;width:448px"></div>

  <h2 class="label label--ingredients">Ingredients</h2>
  <div class="write-line" style="left:910px;top:225px;width:244px"></div>
  <div class="write-line" style="left:700px;top:278px;width:454px"></div>
  <div class="write-line" style="left:700px;top:333px;width:454px"></div>

  <h2 class="label label--instructions">Instructions</h2>
  <div class="write-line" style="left:910px;top:389px;width:244px"></div>
  <div class="write-line" style="left:730px;top:445px;width:424px"></div>
  <div class="write-line" style="left:730px;top:502px;width:424px"></div>
  <div class="write-line" style="left:730px;top:558px;width:424px"></div>
  <div class="write-line" style="left:730px;top:613px;width:424px"></div>
  <div class="write-line" style="left:730px;top:669px;width:424px"></div>
  <div class="write-line" style="left:730px;top:725px;width:424px"></div>
  <div class="write-line" style="left:730px;top:780px;width:424px"></div>
  <div class="write-line" style="left:730px;top:837px;width:424px"></div>

  <p class="website">www.brambleforkpantry.com</p>
</main>
</body>
</html>
```